Business Card design for construction company

I would like a business card design for a construction company - Harlow Constructions. I have attached the ai logo file for use. I would like the card to be very smart and clean and incorporate only white and the two colours in the logo. I would like the card to have two sides. One side can just have the logo, the other with the relevant information.

Target Market(s)

Building and Construction Clients

Industry/Entity Type

Business

Contact Information for Business Card

Name: Tom Pardoe
Company: Harlow Constructions Pty Limited
Address: 14 Mallee Crescent Carrow Vale 2093
Phone: 0427 531 068
Email: tomp@harlowbuild-example.com.au

Font styles to use
Serif
Sans Serif

Requirements
Must have
• Details noted above
• Logo as provided
• Colours as in logo
• Square edges
• A font that compliments the logo
Should not have
• Any colour other than white and those in logo
• Rounded edges

```html
<!DOCTYPE html>
<html lang="en">
<head>
<meta charset="utf-8">
<title>Harlow Constructions – Business Card</title>
<link href="https://fonts.googleapis.com/css2?family=Quicksand:wght@400;500&display=swap" rel="stylesheet">
<style>
  :root {
    --brand-blue: #009fe3;
    --ink: #3b3b3b;
    --paper: #ffffff;
    --backdrop: #e4e4e4;
  }
  * { margin: 0; padding: 0; box-sizing: border-box; }
  html, body {
    width: 1200px; height: 745px; overflow: hidden;
    background: var(--backdrop);
    font-family: "Quicksand", sans-serif;
    color: var(--ink);
  }
  .stage { position: relative; width: 1200px; height: 745px; }

  .card {
    position: absolute;
    width: 520px; height: 289px;
    background: var(--paper);
    overflow: hidden;
    box-shadow: 0 6px 18px rgba(0,0,0,0.12);
  }
  .card--front { left: 50px; top: 228px; }
  .card--back  { left: 630px; top: 228px; }

  .top-band { position: absolute; left: 0; top: 0; width: 100%; background: var(--brand-blue); }
  .card--front .top-band { height: 24px; }
  .card--back .top-band  { height: 12px; }

  .company-name {
    position: absolute; left: 0; right: 0; top: 146px;
    text-align: center;
    font-weight: 400; font-size: 24px; letter-spacing: 5px;
    text-transform: uppercase; color: var(--ink);
  }

  .person {
    position: absolute; right: 20px; top: 34px; text-align: right;
  }
  .person__name {
    font-weight: 400; font-size: 27px; letter-spacing: 1px;
    color: var(--brand-blue); text-transform: uppercase; line-height: 1;
  }
  .person__role { font-weight: 500; font-size: 12px; letter-spacing: 1px; margin-top: 4px; }

  .icon-strip {
    position: absolute; left: 0; bottom: 0; width: 72px; height: 140px;
    background: var(--brand-blue);
  }
  .icon-strip svg { position: absolute; left: 26px; width: 20px; height: 20px; }
  .icon-strip svg * { fill: none; stroke: var(--paper); stroke-width: 1.2; stroke-linejoin: round; stroke-linecap: round; }

  .contact {
    position: absolute; left: 90px; font-weight: 500; font-size: 13px; line-height: 16px; letter-spacing: 0.5px;
  }
  .contact--phone { top: 151px; }
  .contact--email { top: 185px; }
  .contact--web   { top: 214px; }
  .contact--address { top: 246px; }
</style>
</head>
<body>
<div class="stage">

  <section class="card card--front" aria-label="Business card front">
    <div class="top-band"></div>
    <p class="company-name">Harlow Constructions</p>
  </section>

  <section class="card card--back" aria-label="Business card back">
    <div class="top-band"></div>
    <div class="person">
      <p class="person__name">Tom Pardoe</p>
      <p class="person__role">Managing Director</p>
    </div>

    <div class="icon-strip">
      <svg viewBox="0 0 20 20" style="top:14px" aria-label="Phone"><rect x="6" y="2" width="8" height="16" rx="1.5"/><line x1="6" y1="5" x2="14" y2="5"/><line x1="6" y1="15" x2="14" y2="15"/></svg>
      <svg viewBox="0 0 20 20" style="top:44px" aria-label="Email"><rect x="2" y="5" width="16" height="11"/><polyline points="2,5 10,11 18,5"/></svg>
      <svg viewBox="0 0 20 20" style="top:74px" aria-label="Website"><rect x="2" y="4" width="16" height="10"/><line x1="10" y1="14" x2="10" y2="17"/><line x1="6" y1="17" x2="14" y2="17"/></svg>
      <svg viewBox="0 0 20 20" style="top:106px" aria-label="Address"><path d="M10 18 C5 12 4 10 4 8 a6 6 0 0 1 12 0 c0 2 -1 4 -6 10z"/><circle cx="10" cy="8" r="2.2"/></svg>
    </div>

    <p class="contact contact--phone">0427 531 068<br>0427 531 068</p>
    <p class="contact contact--email">info@mail-example.com</p>
    <p class="contact contact--web">www.site-example.com</p>
    <p class="contact contact--address">14 Mallee Crescent<br>Carrow Vale 2093</p>
  </section>

</div>
</body>
</html>
```